A design led business card for the construction industry

High-end business card to match logo. White logo on dark grey/off black to the front. Matching dark font on white to back, possibly with logo design again.

We offer construction and project management services to commercial and private clients in the UK. Projetcs range from newbuilds, conversion of listed buildings and refurbishments and extensions of existing homes. Our focus is on quality and attention to detail using the highest skills.

Contact Information for Business Card

Name; Dylan Marsh BSc
Position; Project Manager
Mobile; 07961 284 657
Tel; 01632 845192
email; dylan@craftvale.co.uk
web; www.craftvale.co.uk
Address; Ashby on Wye, KT4 7PX

Colors

Designer to choose only greyscale colors for use in the design.

Requirements
Must have
• To include the below description of the business,

CONSTRUCTION - PROJECT MANAGEMENT
Nice to have
• The posibility of the top back of the card being used as a ruler. So will have a measurement to scale in mm or an architect scale of 1:50
Should not have
• Should not be portrait

```html
<!DOCTYPE html>
<html lang="en">
<head>
<meta charset="utf-8">
<title>Craft Vale — Business Card</title>
<link rel="stylesheet" href="https://fonts.googleapis.com/css2?family=Poppins:wght@400;500&display=swap">
<style>
  :root {
    --backdrop: #262626;
    --card-light: #ffffff;
    --card-dark: #1d1d1d;
    --ink-dark: #111111;
    --ink-light: #ffffff;
    --ink-muted: #e6e6e6;
  }
  * { box-sizing: border-box; margin: 0; padding: 0; }
  html, body {
    width: 1200px; height: 1200px; overflow: hidden;
    background: var(--backdrop);
    font-family: "Poppins", sans-serif;
  }
  .stage {
    width: 1200px; height: 1200px;
    display: flex; flex-direction: column; align-items: center; justify-content: center;
    gap: 44px;
  }
  .card {
    width: 820px; height: 500px;
    border-radius: 26px;
    position: relative;
    box-shadow: 0 18px 40px rgba(0,0,0,0.35);
  }
  .card--light {
    background: var(--card-light);
    color: var(--ink-dark);
    display: flex; flex-direction: column; align-items: center; justify-content: center;
    gap: 30px;
  }
  .brand-square {
    width: 130px; height: 130px;
    border: 5px solid var(--ink-dark);
  }
  .brand-name {
    font-weight: 400;
    font-size: 30px;
    letter-spacing: 0.55em;
    text-transform: uppercase;
    padding-left: 0.55em;
  }
  .card--dark {
    background: var(--card-dark);
    color: var(--ink-light);
    padding: 56px 64px;
  }
  .card__header {
    font-size: 40px;
    font-weight: 400;
    letter-spacing: 0.5em;
    text-transform: uppercase;
  }
  .person { margin-top: 48px; }
  .person__name {
    font-size: 27px; font-weight: 500; letter-spacing: 0.1em; text-transform: uppercase;
  }
  .person__role {
    font-size: 19px; font-weight: 400; letter-spacing: 0.12em; text-transform: uppercase;
    color: var(--ink-muted);
  }
  .person__rule {
    width: 28px; height: 2px; background: var(--ink-light); margin: 14px 0 18px;
  }
  .contacts { list-style: none; display: flex; flex-direction: column; gap: 6px; }
  .contacts li {
    display: flex; align-items: center; gap: 14px;
    font-size: 21px; font-weight: 400; line-height: 1.25;
  }
  .contacts svg { width: 22px; height: 22px; flex: none; }
  .brand-stack {
    position: absolute; right: 70px; top: 170px;
    width: 280px; height: 280px;
    display: flex; flex-direction: column; justify-content: center; align-items: center;
    font-size: 46px; font-weight: 400; letter-spacing: 0.3em; text-transform: uppercase;
    line-height: 1.4; padding-left: 0.3em;
  }
</style>
</head>
<body>
<main class="stage">
  <section class="card card--light" aria-label="Card back">
    <div class="brand-square" aria-hidden="true"></div>
    <p class="brand-name">Craft Vale</p>
  </section>

  <section class="card card--dark" aria-label="Card front">
    <h1 class="card__header">Craft Vale</h1>
    <div class="person">
      <p class="person__name">Dylan Marsh BSc</p>
      <p class="person__role">Project Manager</p>
      <div class="person__rule"></div>
    </div>
    <ul class="contacts">
      <li>
        <svg viewBox="0 0 22 22" aria-hidden="true"><rect x="1" y="1" width="20" height="20" rx="4" fill="#fff"/><rect x="7" y="4.5" width="8" height="13" rx="1.5" fill="none" stroke="#1d1d1d" stroke-width="1.8"/></svg>
        07961 284 657
      </li>
      <li>
        <svg viewBox="0 0 22 22" aria-hidden="true"><rect x="1" y="1" width="20" height="20" rx="4" fill="#fff"/><path d="M6.5 5.5c1-.6 2 .1 2.4 1.1l.5 1.4c.2.6-.1 1.1-.6 1.5l-.6.4c.7 1.6 1.8 2.7 3.4 3.4l.4-.6c.4-.5.9-.8 1.500-.6l1.4.5c1 .4 1.7 1.4 1.1 2.4-.7 1.1-2 1.6-3.3 1.1C9.7 15.1 6.9 12.3 5.4 8.8 4.9 7.5 5.4 6.2 6.5 5.5z" fill="#1d1d1d"/></svg>
        01632 845192
      </li>
      <li>
        <svg viewBox="0 0 22 22" aria-hidden="true"><rect x="1" y="1" width="20" height="20" rx="4" fill="#fff"/><rect x="4.5" y="6.5" width="13" height="9" fill="none" stroke="#1d1d1d" stroke-width="1.6"/><path d="M4.5 6.5l6.5 5 6.5-5" fill="none" stroke="#1d1d1d" stroke-width="1.6"/></svg>
        dylan@craftvale.co.uk
      </li>
      <li>
        <svg viewBox="0 0 22 22" aria-hidden="true"><rect x="1" y="1" width="20" height="20" rx="4" fill="#fff"/><circle cx="11" cy="11" r="6" fill="none" stroke="#1d1d1d" stroke-width="1.5"/><ellipse cx="11" cy="11" rx="2.6" ry="6" fill="none" stroke="#1d1d1d" stroke-width="1.3"/><path d="M5 11h12M6 8h10M6 14h10" stroke="#1d1d1d" stroke-width="1.2"/></svg>
        www.craftvale.co.uk
      </li>
      <li>
        <svg viewBox="0 0 22 22" aria-hidden="true"><rect x="1" y="1" width="20" height="20" rx="4" fill="#fff"/><path d="M11 4.5a4.5 4.5 0 0 1 4.5 4.5c0 3.3-4.5 8.5-4.5 8.5S6.5 12.3 6.5 9A4.5 4.5 0 0 1 11 4.5z" fill="#1d1d1d"/><circle cx="11" cy="9" r="1.7" fill="#fff"/></svg>
        Ashby on Wye, KT4 7PX
      </li>
    </ul>
    <div class="brand-stack"><span>Craft</span><span>Vale</span></div>
  </section>
</main>
</body>
</html>
```